Artisan Bread Company needs a business card

I need a business card design, for an artisan bread company called "Holloway's Bread".

I would like the logo on one side, and on the other, I would like it to say

Dorian Holloway
Baker
416.552.0193
hollowaysbread@breadmail.example

Not necessarily in that order- but it must have these.

Industry/Entity Type

Business

Font styles to use
Serif

Requirements
Must have
• The provided logo on the front, this on the back-
• Dorian Holloway
• Baker
• 416.552.0193
• hollowaysbread@breadmail.example

```html
<!DOCTYPE html>
<html lang="en">
<head>
<meta charset="utf-8">
<title>Holloway's Bread — Business Card</title>
<link rel="stylesheet" href="https://fonts.googleapis.com/css2?family=Montserrat:wght@400;600;700&display=swap">
<style>
  :root {
    --backdrop: #4a4846;
    --card-dark: #2e2c2a;
    --card-cream: #edebdf;
    --ink: #1f1d1b;
    --ink-soft: #4b4945;
    --cream-text: #e6e2d3;
  }
  * { box-sizing: border-box; margin: 0; padding: 0; }
  html, body {
    width: 1200px; height: 786px; overflow: hidden;
    background: var(--backdrop);
    font-family: "Montserrat", sans-serif;
  }
  .canvas {
    width: 1200px; height: 786px;
    display: flex; align-items: center; justify-content: center; gap: 40px;
  }
  .card {
    width: 530px; height: 303px;
    border-radius: 18px;
    box-shadow: 0 14px 30px rgba(0,0,0,.35);
    position: relative;
  }
  .card--front {
    background: var(--card-dark);
    display: flex; align-items: center; justify-content: center;
  }
  .card--back {
    background: var(--card-cream);
    display: flex; align-items: center;
    padding: 0 36px 0 40px;
  }
  .brand-name {
    font-weight: 400;
    letter-spacing: .04em;
  }
  .card--front .brand-name { color: var(--cream-text); font-size: 38px; }
  .card--back .brand-name { color: var(--ink); font-size: 25px; width: 210px; line-height: 1.2; }
  .contact { margin-left: 26px; color: var(--ink); }
  .contact__name {
    font-weight: 700; font-size: 15px; letter-spacing: .06em; text-transform: uppercase;
  }
  .contact__role { font-size: 12px; color: var(--ink-soft); margin: 3px 0 16px; }
  .contact__line {
    display: flex; align-items: center; gap: 8px;
    font-size: 12px; margin-top: 5px;
  }
  .contact__line svg { width: 12px; height: 12px; flex: none; }
</style>
</head>
<body>
  <main class="canvas">
    <section class="card card--front" aria-label="Card front">
      <p class="brand-name">Holloway's Bread</p>
    </section>

    <section class="card card--back" aria-label="Card back">
      <p class="brand-name">Holloway's Bread</p>
      <div class="contact">
        <p class="contact__name">Dorian Holloway</p>
        <p class="contact__role">Baker</p>
        <p class="contact__line">
          <svg viewBox="0 0 24 24" aria-hidden="true"><path fill="#1f1d1b" d="M6.6 10.8a15.1 15.1 0 0 0 6.6 6.6l2.2-2.2a1 1 0 0 1 1-.25 11.4 11.4 0 0 0 3.6.57 1 1 0 0 1 1 1V20a1 1 0 0 1-1 1A17 17 0 0 1 3 4a1 1 0 0 1 1-1h3.5a1 1 0 0 1 1 1c0 1.25.2 2.45.57 3.6a1 1 0 0 1-.25 1z"/></svg>
          <span>416.552.0193</span>
        </p>
        <p class="contact__line">
          <svg viewBox="0 0 24 24" aria-hidden="true"><path fill="#1f1d1b" d="M3 5h18a1 1 0 0 1 1 1v12a1 1 0 0 1-1 1H3a1 1 0 0 1-1-1V6a1 1 0 0 1 1-1zm9 7.5L20 7H4z"/></svg>
          <span>hollowaysbread@breadmail.example</span>
        </p>
      </div>
    </section>
  </main>
</body>
</html>
```